Letterhead for Business Law Firm

We need a letter head for our firm based on the design we have settled on and it is attached. Our clients are small and large businesses around the world, and our letterhead is used typically for formal legal purposes such as demand letters (accusing the recipient of doing bad things) or responding to demand letters. It may also be sent to regulators and other government agencies. So this needs to be tasteful, but a little edgy as well - we try to convey that we are a firm that is different - businesses and investors come to us for creative, quick advice, typically in high stress circumstances, and for our ability to work through high conflict situations, and rapid paced engagements.

Target Market(s)

Lawyers, business executives, investors, government regulators who may receive letters from this firm on behalf of its clients.

Industry/Entity Type

Business

Requirements
Must have
• The design and the firm's contact information:
• Quillfen Law Firm, P.C.
• 8716 SW 19th Ave
• Portland, OR 97058
• phone: 971 555 0143
• fax: 971 555 0178
• in what placement and how depicted (e.g. a phone icon instead of the word "phone") I leave to your creative ideas.
Nice to have
• design and information can be placed at the top, bottom and/or sides of the letter, and the design should be for a standard letter size paper - and can have a separate design for the second page.

```html
<!DOCTYPE html>
<html lang="en">
<head>
<meta charset="utf-8">
<title>Quillfen Law Firm, P.C. Letterhead</title>
<link href="https://fonts.googleapis.com/css2?family=Barlow:wght@400;500&display=swap" rel="stylesheet">
<style>
  :root {
    --paper: #ffffff;
    --ink: #1a1a1a;
    --text: #333333;
    --rule: #8a8a8a;
    --accent: #3b7c84;
  }
  * { margin: 0; padding: 0; box-sizing: border-box; }
  html, body {
    width: 845px;
    height: 1200px;
    overflow: hidden;
    background: var(--paper);
  }
  .letterhead {
    position: relative;
    width: 845px;
    height: 1200px;
    border: 1px solid var(--rule);
    font-family: "Barlow", Arial, sans-serif;
    color: var(--text);
  }
  .brand {
    position: absolute;
    left: 17px;
    top: 17px;
    height: 67px;
    display: flex;
    align-items: center;
    gap: 14px;
  }
  .brand-square {
    width: 40px;
    height: 40px;
    background: var(--accent);
  }
  .brand-name {
    font-size: 38px;
    font-weight: 400;
    letter-spacing: 7px;
    color: var(--ink);
    text-transform: uppercase;
  }
  .contact {
    position: absolute;
    right: 20px;
    top: 18px;
    list-style: none;
  }
  .contact-item {
    display: flex;
    align-items: center;
    height: 20px;
    font-size: 13px;
    font-weight: 400;
    color: var(--text);
    white-space: nowrap;
  }
  .contact-icon {
    width: 16px;
    height: 16px;
    margin-right: 9px;
    flex: none;
  }
  .footer-rule {
    position: absolute;
    left: 0;
    right: 0;
    top: 1147px;
    border-top: 1px solid var(--rule);
  }
  .footer-address {
    position: absolute;
    left: 0;
    right: 0;
    top: 1161px;
    text-align: center;
    font-size: 13px;
    font-weight: 400;
    color: var(--text);
    white-space: nowrap;
  }
</style>
</head>
<body>
<div class="letterhead">
  <header class="brand">
    <span class="brand-square"></span>
    <span class="brand-name">Quillfen</span>
  </header>

  <ul class="contact">
    <li class="contact-item">
      <svg class="contact-icon" viewBox="0 0 16 16" aria-hidden="true">
        <circle cx="8" cy="8" r="8" fill="var(--ink)"/>
        <path d="M5.2 4.3c.4-.3.9-.2 1.1.2l.7 1.3c.2.4.1.8-.2 1l-.5.4c.4 1 1.1 1.8 2.1 2.3l.5-.5c.3-.3.7-.3 1-.1l1.2.8c.4.3.4.8.1 1.1l-.7.7c-.5.5-1.3.5-2 .2C6.4 10.6 5 9.1 4.3 7.2c-.3-.8-.2-1.6.3-2.2z" fill="#fff"/>
      </svg>
      971 555 0143
    </li>
    <li class="contact-item">
      <svg class="contact-icon" viewBox="0 0 16 16" aria-hidden="true">
        <circle cx="8" cy="8" r="8" fill="var(--ink)"/>
        <g fill="none" stroke="#fff" stroke-width="1">
          <rect x="5.5" y="3.8" width="5" height="3"/>
          <rect x="4" y="6.8" width="8" height="4"/>
          <rect x="5.5" y="9.4" width="5" height="2.8" fill="var(--ink)"/>
        </g>
      </svg>
      971 555 0178
    </li>
    <li class="contact-item">
      <svg class="contact-icon" viewBox="0 0 16 16" aria-hidden="true">
        <circle cx="8" cy="8" r="8" fill="var(--ink)"/>
        <rect x="4" y="5.2" width="8" height="5.6" fill="none" stroke="#fff" stroke-width="1.1"/>
        <path d="M4 5.4l4 3 4-3" fill="none" stroke="#fff" stroke-width="1.1"/>
      </svg>
      info@quillfen.com
    </li>
    <li class="contact-item">
      <svg class="contact-icon" viewBox="0 0 16 16" aria-hidden="true">
        <circle cx="8" cy="8" r="8" fill="var(--ink)"/>
        <g fill="none" stroke="#fff" stroke-width="0.9">
          <circle cx="8" cy="8" r="4.6"/>
          <ellipse cx="8" cy="8" rx="2" ry="4.6"/>
          <path d="M3.4 8h9.2M4.1 5.8h7.8M4.1 10.2h7.8"/>
        </g>
      </svg>
      www.quillfen.com
    </li>
  </ul>

  <div class="footer-rule"></div>
  <footer class="footer-address">Quillfen Law Firm, P.C. &middot; 8716 SW 19th Ave, Portland, OR 97058</footer>
</div>
</body>
</html>
```